Luminously Grounded Vitality

We want to design a business card that is modern and appealing for an innovative psychedelic telemedicine company that provides at-home ketamine-assisted therapy along with wellness, longevity, and anti-aging medicines. We want to use our deep purple and white plus other colors you can find on our website. We don't have any strict brand guidelines yet so feel free to get creative. We want a very professional, but technology first modern design that will instill trust, peace, calm, but also be attractive to investors in the healthcare and SaaS space.

```html
<!DOCTYPE html>
<html lang="en">
<head>
<meta charset="utf-8">
<title>Luminously — Business Card</title>
<link rel="stylesheet" href="https://fonts.googleapis.com/css2?family=Montserrat:wght@400;500;700&family=Tenor+Sans&display=swap">
<style>
  :root {
    --stage: #3a3a3a;
    --stage-deep: #2b2b2b;
    --card: #151515;
    --card-edge: #b56fb0;
    --purple: #8a6bc4;
    --orchid: #c77cbf;
    --white: #f2f2f2;
    --divider: #6c5aa8;
    --mark-tone: #1f1f1f;
  }
  * { box-sizing: border-box; margin: 0; padding: 0; }
  html, body { width: 1200px; height: 801px; overflow: hidden; }
  body {
    background: radial-gradient(ellipse at 50% 40%, var(--stage) 0%, var(--stage-deep) 100%);
    position: relative;
  }
  .card {
    position: absolute;
    top: 256px;
    width: 504px;
    height: 288px;
    background: var(--card);
    border-bottom: 2px solid var(--card-edge);
    box-shadow: 0 12px 30px rgba(0,0,0,.45);
    overflow: hidden;
  }
  .card--back { left: 66px; }
  .card--front { left: 630px; }

  .wordmark {
    font-family: "Tenor Sans", sans-serif;
    color: var(--orchid);
    letter-spacing: .5px;
    white-space: nowrap;
  }

  /* contact side */
  .back__badge {
    position: absolute;
    left: 46px;
    top: 92px;
    width: 72px;
    height: 72px;
    border-radius: 50%;
    background: var(--purple);
  }
  .back__brand {
    position: absolute;
    left: 36px;
    top: 190px;
  }
  .back__brand .wordmark { font-size: 34px; }
  .back__divider {
    position: absolute;
    left: 262px;
    top: 38px;
    width: 1px;
    height: 128px;
    background: var(--divider);
  }
  .contact {
    position: absolute;
    left: 284px;
    top: 38px;
    font-family: "Montserrat", sans-serif;
    color: var(--white);
  }
  .contact__name {
    font-weight: 700;
    font-size: 17px;
    color: var(--purple);
    letter-spacing: .3px;
    text-transform: uppercase;
  }
  .contact__role {
    font-size: 11px;
    color: var(--orchid);
    margin-top: 1px;
  }
  .contact__address {
    font-size: 11.5px;
    line-height: 1.45;
    margin-top: 14px;
  }
  .contact__lines {
    list-style: none;
    margin-top: 14px;
    font-size: 11.5px;
    line-height: 1.6;
  }
  .contact__lines li { display: flex; align-items: center; gap: 6px; }
  .contact__lines svg { width: 10px; height: 10px; fill: var(--orchid); flex: none; }

  /* brand side */
  .front__mark {
    position: absolute;
    left: 32px;
    top: 54px;
    width: 180px;
    height: 180px;
    border-radius: 50%;
    background: var(--mark-tone);
  }
  .front__brand {
    position: absolute;
    right: 34px;
    top: 152px;
  }
  .front__brand .wordmark { font-size: 38px; }
</style>
</head>
<body>

<section class="card card--back" aria-label="Card contact side">
  <span class="back__badge"></span>
  <div class="back__brand">
    <span class="wordmark">Luminously</span>
  </div>
  <div class="back__divider"></div>
  <div class="contact">
    <p class="contact__name">Mara Quillen</p>
    <p class="contact__role">President</p>
    <p class="contact__address">1480 Seabright Cove Rd<br>Coral Haven CA 92011</p>
    <ul class="contact__lines">
      <li>
        <svg viewBox="0 0 10 10" aria-hidden="true"><path d="M2 0.5 L3.8 2.6 L2.9 3.7 Q4 6 6.3 7.1 L7.4 6.2 L9.5 8 L8.3 9.5 Q1.5 8.6 0.5 1.7 Z"/></svg>
        555-014-2278
      </li>
      <li>
        <svg viewBox="0 0 10 10" aria-hidden="true"><path d="M0.5 2 H9.5 V8.5 H0.5 Z M1 2.4 L5 5.6 L9 2.4" fill="var(--orchid)" stroke="var(--card)" stroke-width=".8"/></svg>
        hello@luminouslyvitality.com
      </li>
      <li>
        <svg viewBox="0 0 10 10" aria-hidden="true"><circle cx="5" cy="5" r="4.5"/><path d="M0.5 5 H9.5 M5 0.5 Q2.5 5 5 9.5 M5 0.5 Q7.5 5 5 9.5" fill="none" stroke="var(--card)" stroke-width=".7"/></svg>
        www.luminouslyvitality.com
      </li>
    </ul>
  </div>
</section>

<section class="card card--front" aria-label="Card brand side">
  <span class="front__mark"></span>
  <div class="front__brand">
    <span class="wordmark">Luminously</span>
  </div>
</section>

</body>
</html>
```